Zielgruppe
Ich biete die neue Dienstleistung an, Schulungen zu überprüfen auf deren Inhalt und mittels einem Zertifikat zu bestätigen, dass die geprüfte Schulung allen notwendigen Anforderungen der Normen und Regelwerke in Sachen Gaswarntechnik entspricht.
Daraufhin darf der Geprüfte (Schulungsanbieter/Schulungsgesellschaften) mit meinem Siegel für seine Schulumng werben.
Dies wird ausschießlich für Schulungen von Gaswarntechnik angeboten von mir angeboten. Das Siegel existiert schon und das Zertifikat sollte hier mit integriert werden.
Aufgabenstellung
Ich stelle mir ein hochwertiges Design vor, eine einzige DIN A4 Seite und 3D-Effekt. Es muss richtig teuer, hochwertig und modern aussehen, sodass man auch fühlt, dass es eine Wertigkeit hat. Das bestehende Siegel sollte integriert werden.
Ich brauche Textteile die ich anpassen kann. Zum einen muss ein Bereich da sein wo ich die Bezeichnung der geprüften Schulungen unterbringen kann, dann ein Bereich wo ich etwas zum Inhalt/Prüfung schreiben kann und natürlich Datum und Unterschriftsfeld. Das Zertifikat hat immer eine Gültigkeit von 2 Jahren ab Ausstellungsdatum.
Es sollten meine Farben eingsetzt werden. Zum einen ist dies
Ultramarinblau RAL 5002 RGB= rot 0/grün 56/ blau 123
Weiß
gelb (nicht genau definiert), rapsgelb RAL 1021/1023
Schriftart Verdana
Das Design sollte an mein bestehndes Design in Sachen Logo/Homepage angelehnt sein.

```html
<!DOCTYPE html>
<html lang="de">
<head>
<meta charset="utf-8">
<title>Zertifikat</title>
<link rel="stylesheet" href="https://fonts.googleapis.com/css2?family=Noto+Sans:wght@400;700;800&display=swap">
<style>
  :root {
    --ultramarine: #00387b;
    --ultramarine-light: #0a5d96;
    --steel: #8aa3b8;
    --gold: #b8893a;
    --gold-light: #f0dca0;
    --gold-dark: #8f6a2a;
    --ink: #3a4250;
    --paper: #f3f4f7;
    --shade: #e3e5ec;
  }
  * { margin: 0; padding: 0; box-sizing: border-box; }
  html, body { width: 1200px; height: 848px; overflow: hidden; background: var(--paper); }
  body { font-family: Verdana, "Noto Sans", sans-serif; }
  .certificate { position: relative; width: 1200px; height: 848px; overflow: hidden; }
  .backdrop {
    position: absolute; inset: 0;
    background: linear-gradient(160deg, #e6e8ee 0%, #f6f7f9 35%, #f3f4f7 65%, #e4e6ec 100%);
  }
  .title {
    position: absolute; left: 119px; top: 232px;
    font-size: 94px; font-weight: 800; letter-spacing: 7px; line-height: 1;
    background: linear-gradient(90deg, var(--ultramarine) 0%, var(--ultramarine-light) 70%, var(--steel) 100%);
    -webkit-background-clip: text; background-clip: text; color: transparent;
  }
  .presented {
    position: absolute; left: 112px; top: 346px; width: 512px; height: 44px;
    border-radius: 22px;
    background: linear-gradient(90deg, #0a5d96, var(--ultramarine) 60%, #1b6eb0);
    color: var(--gold-light); font-size: 16px; font-weight: 700; letter-spacing: 1.6px;
    display: flex; align-items: center; justify-content: center;
  }
  .recipient {
    position: absolute; left: 118px; top: 452px;
    font-size: 58px; font-weight: 700; color: var(--ultramarine-light); line-height: 1;
  }
  .gold-rule {
    position: absolute; height: 3px;
    background: linear-gradient(90deg, var(--gold-dark), var(--gold-light) 50%, var(--gold));
  }
  .recipient-rule { left: 117px; top: 531px; width: 642px; }
  .course-title {
    position: absolute; left: 118px; top: 580px;
    font-size: 16px; font-weight: 700; color: var(--gold); letter-spacing: 1.1px;
  }
  .course-text {
    position: absolute; left: 118px; top: 616px; width: 585px;
    font-size: 11px; font-weight: 700; line-height: 1.7; color: var(--ink);
  }
  .validity {
    position: absolute; left: 118px; top: 733px;
    font-size: 10px; font-weight: 700; line-height: 1.4; color: #6b7280; letter-spacing: .5px;
  }
  .seal {
    position: absolute; left: 918px; top: 121px; width: 135px; height: 178px;
    background: linear-gradient(160deg, #f7b21c, #e59a05 60%, #c87f00);
    border: 4px solid #fff; box-shadow: 0 4px 14px rgba(0,0,0,.25);
  }
  .signature {
    position: absolute; left: 905px; width: 160px; height: 50px;
    background: linear-gradient(90deg, rgba(60,70,90,.15), rgba(60,70,90,.3), rgba(60,70,90,.1));
    border-radius: 25px;
  }
  .signature-date { top: 378px; }
  .signature-name { top: 530px; }
  .sign-rule { left: 872px; width: 227px; height: 2px; }
  .sign-rule-date { top: 434px; }
  .sign-rule-name { top: 588px; }
  .sign-label {
    position: absolute; left: 872px; width: 227px; text-align: center;
    font-size: 14px; font-weight: 700; color: var(--ink); letter-spacing: 1.5px;
  }
  .label-date { top: 446px; }
  .label-name { top: 604px; }
  .brand {
    position: absolute; left: 902px; top: 768px;
    display: flex; align-items: center; gap: 10px;
  }
  .brand-dot { width: 34px; height: 34px; border-radius: 50%; background: var(--ultramarine); }
  .brand-name { font-size: 24px; font-weight: 700; color: var(--ultramarine); }
</style>
</head>
<body>
<main class="certificate">
  <div class="backdrop" role="img" aria-label="Hintergrund mit hellen Flächen und goldenen Diagonalbändern"></div>

  <h1 class="title">ZERTIFIKAT</h1>
  <div class="presented">THIS CERTIFICATE PROUDLY PRESENTED TO</div>
  <p class="recipient">Name Nachname</p>
  <div class="gold-rule recipient-rule"></div>
  <h2 class="course-title">LOREM IPSUM DOLOR SIT AMET, CONSECTETUR ADIPISCING ELIT SED DO.</h2>
  <p class="course-text">Lorem ipsum dolor sit amet, consectetur adipiscing elit, sed do eiusmod tempor incididunt ut labore et dolore magna aliqua. Ut enim ad minim veniam, quis nostrud exercitation ullamco laboris nisi ut aliquip ex ea commodo consequat.</p>
  <p class="validity">GÜLTIG: 2 JAHRE AB<br>AUSSTELLUNGSDATUM</p>

  <div class="seal" role="img" aria-label="Qualitätssiegel Schulung"></div>

  <div class="signature signature-date" role="img" aria-label="Unterschrift"></div>
  <div class="gold-rule sign-rule sign-rule-date"></div>
  <p class="sign-label label-date">DATUM</p>

  <div class="signature signature-name" role="img" aria-label="Unterschrift"></div>
  <div class="gold-rule sign-rule sign-rule-name"></div>
  <p class="sign-label label-name">NAME SURNAME</p>

  <div class="brand">
    <span class="brand-dot"></span>
    <span class="brand-name">Sensorik-Kontor</span>
  </div>
</main>
</body>
</html>
```